Need Business cards

Im a new realtor and already have a logo. I would like to purchase a Business card design that catches customer's attention, its creative, and modern.

Marisol Vandera
Realtor ®
(555) 214 7730
marisolvndrealtor@brightmailbox.com

Target Market(s)

investors, buyers and seller, property management

Industry/Entity Type

real estate,

Contact Information for Business Card

Marisol Vandera

Requirements
Must have
• BOTH LOGOS, WOULD LIKE TO SEE WITH DIFFERENT OPTIONS WITH EITHER PICTURE

```html
<!DOCTYPE html>
<html lang="en">
<head>
<meta charset="utf-8">
<title>Marisol Vandera – Realtor Business Card</title>
<link rel="stylesheet" href="https://fonts.googleapis.com/css2?family=Raleway:wght@500;700&family=Open+Sans:wght@400&display=swap">
<style>
  :root {
    --backdrop: #969696;
    --card-white: #f7f7f5;
    --card-black: #0c0c0c;
    --gold: #c9a227;
    --gold-deep: #b08a1c;
    --text-grey: #6b6b6b;
    --title-grey: #7a7a7a;
    --broker-blue: #4f84c9;
    --white: #ffffff;
  }
  * { box-sizing: border-box; margin: 0; padding: 0; }
  html, body {
    width: 1200px; height: 1016px; overflow: hidden;
    background: var(--backdrop);
  }
  .sheet {
    position: relative; width: 1200px; height: 1016px;
    display: flex; flex-direction: column; align-items: center; justify-content: center; gap: 56px;
  }
  .card {
    position: relative; width: 630px; height: 360px; overflow: hidden;
    box-shadow: 0 14px 30px rgba(0,0,0,.28);
  }

  /* Front */
  .card--front {
    background: var(--card-white);
    display: flex; flex-direction: column; align-items: center;
    padding-top: 34px;
    text-align: center;
  }
  .brand-mark {
    display: flex; align-items: center; gap: 10px;
    padding: 8px 20px;
    border-top: 1px solid var(--gold);
    border-bottom: 1px solid var(--gold);
  }
  .brand-mark__square { width: 12px; height: 12px; background: var(--gold); }
  .brand-mark__name {
    font-family: "Raleway", sans-serif; font-weight: 500;
    font-size: 24px; letter-spacing: 3px; text-transform: uppercase;
    color: var(--gold);
  }
  .agent-name {
    margin-top: 24px;
    font-family: "Raleway", sans-serif; font-weight: 700;
    font-size: 25px; color: var(--gold-deep);
  }
  .agent-title {
    font-family: "Raleway", sans-serif; font-weight: 700;
    font-size: 20px; color: var(--title-grey);
  }
  .agent-title sup { font-size: 9px; }
  .contact-icons { display: flex; gap: 18px; margin: 10px 0 6px; }
  .contact-icons svg { width: 18px; height: 18px; }
  .contact-line {
    font-family: "Open Sans", sans-serif; font-weight: 400;
    font-size: 16px; line-height: 1.3; color: var(--text-grey);
  }
  .brokerage {
    margin-top: 16px;
    display: flex; align-items: center; gap: 8px;
  }
  .brokerage__square { width: 10px; height: 10px; background: var(--broker-blue); }
  .brokerage__name {
    font-family: "Raleway", sans-serif; font-weight: 700;
    font-size: 24px; letter-spacing: 2px; text-transform: uppercase;
    color: var(--broker-blue);
  }

  /* Back */
  .card--back { background: var(--card-black); }
  .portrait {
    position: absolute; left: 48px; top: 0; width: 560px; height: 296px;
    background: radial-gradient(ellipse at 38% 55%, #d9c6a2 0%, #c9b48d 30%, #3b352c 62%, #0c0c0c 85%);
  }
  .back-signature {
    position: absolute; right: 34px; bottom: 14px; text-align: right;
    font-family: "Raleway", sans-serif; color: var(--white);
  }
  .back-signature__name { font-weight: 700; font-size: 24px; letter-spacing: .5px; }
  .back-signature__title { font-weight: 700; font-size: 17px; margin-top: -2px; }
  .back-signature__title sup { font-size: 8px; }
</style>
</head>
<body>
<main class="sheet">
  <section class="card card--front" aria-label="Card front">
    <div class="brand-mark">
      <span class="brand-mark__square"></span>
      <span class="brand-mark__name">Marisol Vandera</span>
    </div>
    <h1 class="agent-name">Marisol Vandera</h1>
    <p class="agent-title">Realtor<sup>®</sup></p>
    <div class="contact-icons">
      <svg viewBox="0 0 24 24" aria-label="Phone"><path fill="var(--gold)" d="M6.6 10.8a15.1 15.1 0 0 0 6.6 6.6l2.2-2.2a1 1 0 0 1 1-.25 11.4 11.4 0 0 0 3.6.57 1 1 0 0 1 1 1V20a1 1 0 0 1-1 1A17 17 0 0 1 3 4a1 1 0 0 1 1-1h3.5a1 1 0 0 1 1 1c0 1.25.2 2.45.57 3.57a1 1 0 0 1-.25 1z"/></svg>
      <svg viewBox="0 0 24 24" aria-label="Email"><rect x="2" y="5" width="20" height="14" rx="1.5" fill="var(--gold)"/><path d="M3 6l9 7 9-7" fill="none" stroke="var(--card-white)" stroke-width="1.5"/></svg>
      <svg viewBox="0 0 24 24" aria-label="Website"><g fill="none" stroke="var(--gold)" stroke-width="1.8"><circle cx="12" cy="12" r="9"/><ellipse cx="12" cy="12" rx="4" ry="9"/><path d="M3 12h18M4.5 7.5h15M4.5 16.5h15"/></g></svg>
    </div>
    <p class="contact-line">(555) 214 7730</p>
    <p class="contact-line">marisolvndrealtor@brightmailbox.com</p>
    <p class="contact-line">www.marisolvandera-homes.com</p>
    <div class="brokerage">
      <span class="brokerage__square"></span>
      <span class="brokerage__name">Crestline Realty</span>
    </div>
  </section>

  <section class="card card--back" aria-label="Card back">
    <div class="portrait" role="img" aria-label="Portrait photograph of the realtor in a cream blazer against a black background"></div>
    <div class="back-signature">
      <p class="back-signature__name">MARISOL VANDERA</p>
      <p class="back-signature__title">Realtor<sup>®</sup></p>
    </div>
  </section>
</main>
</body>
</html>
```